TEK Logistics - Banner 2.5' x 8' for 20+ locations

Need a banner designed that will pop. This banner will be displayed at over 20 of our transportation facilities. Goal is for the banner to grab the attention of employees, contractors and clients and help reinforce our mission and core values. Designed needs to include TEK Logo, our core values and mission statement. Red and Black are the main company colors and we need to stay within that theme and color pallet. Attached is a previous version that was too basic and boring. Willing to consider a design that excludes the mission statement.

Gathering more feedback

```html
<!DOCTYPE html>
<html lang="en">
<head>
<meta charset="utf-8">
<title>TEK Logistics – Core Values Banner</title>
<link rel="stylesheet" href="https://fonts.googleapis.com/css2?family=Saira:wght@400;500;700&display=swap">
<style>
  :root {
    --brand-red: #bd2026;
    --brand-red-deep: #8e1419;
    --brand-black: #2f2c2c;
    --mission-dark: #3a1414;
    --wall-light: #f2f2f2;
    --wall-shade: #dcdcdc;
    --text-light: #ffffff;
    --dot-fill: #ffffff;
  }
  html, body {
    margin: 0;
    padding: 0;
    overflow: hidden;
    background: #ffffff;
  }
  .banner {
    position: relative;
    width: 1200px;
    height: 375px;
    overflow: hidden;
    font-family: "Saira", sans-serif;
  }
  .banner__wall {
    position: absolute;
    inset: 0;
    background: radial-gradient(ellipse at 50% 45%, var(--wall-light) 0%, var(--wall-shade) 100%);
  }
  .banner__art {
    position: absolute;
    inset: 0;
    width: 1200px;
    height: 375px;
  }
  .value-band--red { fill: var(--brand-red); }
  .value-band--black { fill: var(--brand-black); }
  .value-dot { fill: var(--dot-fill); stroke-width: 3; }
  .value-dot--on-red { stroke: var(--brand-red-deep); }
  .value-dot--on-black { stroke: var(--brand-black); }
  .value-text {
    fill: var(--text-light);
    font-family: "Saira", sans-serif;
    font-size: 31px;
    font-weight: 500;
  }
  .brand-name {
    fill: var(--brand-red);
    font-family: "Saira", sans-serif;
    font-size: 52px;
    font-weight: 700;
  }
  .mission-label {
    fill: var(--text-light);
    font-family: "Saira", sans-serif;
    font-weight: 400;
  }
  .mission-label--small { font-size: 30px; }
  .mission-label--large { font-size: 58px; letter-spacing: 6px; }
  .mission-text {
    fill: var(--text-light);
    font-family: "Saira", sans-serif;
    font-size: 23.5px;
    font-weight: 500;
  }
</style>
</head>
<body>
<div class="banner">
  <div class="banner__wall" role="img" aria-label="Whitewashed brick wall background"></div>

  <svg class="banner__art" viewBox="0 0 1440 450" xmlns="http://www.w3.org/2000/svg">
    <defs>
      <linearGradient id="mission-fill" x1="1" y1="0" x2="0" y2="1">
        <stop offset="0" stop-color="var(--brand-red)"/>
        <stop offset="0.45" stop-color="var(--brand-red-deep)"/>
        <stop offset="1" stop-color="var(--mission-dark)"/>
      </linearGradient>
    </defs>

    <!-- Brand name -->
    <text class="brand-name" x="180" y="243" text-anchor="middle">TEK Logistics</text>

    <!-- Mission panel -->
    <path class="mission-panel" fill="url(#mission-fill)"
          d="M1005 428 L1005 140 Q1005 22 1125 22 L1410 22 L1410 320 Q1410 385 1345 385 L1345 428 Z"/>

    <!-- Core value bands -->
    <g class="core-values">
      <polygon class="value-band value-band--red" points="280,33 1120,33 1095,82 335,82"/>
      <circle class="value-dot value-dot--on-red" cx="327" cy="57" r="13"/>
      <text class="value-text" x="388" y="68">Do the right things for the right reasons</text>

      <polygon class="value-band value-band--black" points="368,99 1035,99 1020,148 400,148"/>
      <circle class="value-dot value-dot--on-black" cx="386" cy="125" r="13"/>
      <text class="value-text" x="440" y="135">Pursue growth and development</text>

      <polygon class="value-band value-band--red" points="398,166 1000,166 1000,216 412,216"/>
      <circle class="value-dot value-dot--on-red" cx="408" cy="190" r="13"/>
      <text class="value-text" x="452" y="201">Build a positive team atmosphere</text>

      <polygon class="value-band value-band--black" points="412,233 995,233 995,282 398,282"/>
      <circle class="value-dot value-dot--on-black" cx="408" cy="258" r="13"/>
      <text class="value-text" x="460" y="268">Deliver WOW through service</text>

      <polygon class="value-band value-band--red" points="400,300 995,300 995,350 368,350"/>
      <circle class="value-dot value-dot--on-red" cx="386" cy="324" r="13"/>
      <text class="value-text" x="440" y="335">Do everything Safely</text>

      <polygon class="value-band value-band--black" points="335,367 995,367 995,416 280,416"/>
      <circle class="value-dot value-dot--on-black" cx="327" cy="392" r="13"/>
      <text class="value-text" x="388" y="402">Have Fun</text>
    </g>

    <!-- Mission heading -->
    <text class="mission-label mission-label--small" transform="translate(1050 378) rotate(-90)">our</text>
    <text class="mission-label mission-label--large" transform="translate(1094 378) rotate(-90)">MISSION</text>

    <!-- Mission statement -->
    <text class="mission-text" x="1108" y="126">
      <tspan x="1108" dy="0">Provide the best</tspan>
      <tspan x="1108" dy="30.5">customer experience</tspan>
      <tspan x="1108" dy="30.5">while creating an</tspan>
      <tspan x="1108" dy="30.5">environment of</tspan>
      <tspan x="1108" dy="30.5">growth and</tspan>
      <tspan x="1108" dy="30.5">opportunity for our</tspan>
      <tspan x="1108" dy="30.5">customers,</tspan>
      <tspan x="1108" dy="30.5">employees, and</tspan>
      <tspan x="1108" dy="30.5">service providers.</tspan>
    </text>
  </svg>
</div>
</body>
</html>
```